Norvale Email Signature Banners – Fabrication Capability Series

www.Norvale.com.au is an Australian engineering and fabrication company specialising in fabrication and welding of :
steel piping spools,
skids and frames,
small volume process steel tanks
and general steel fabrication
We require four distinct banner designs for use in Teldrin Quillmark email signatures. Each banner will highlight a specific capability while maintaining a consistent brand identity.
Deliverables
Four banners total:
Piping Spools Fabrication – focus on precision welding and stainless steel pipework
Skid & Frames Fabrication – highlight skid systems and structural frames
Small Steel Tanks Fabrication – show fabricated tanks and workshop craftsmanship
General Fabrication Solutions – broad steel fabrication theme for company-wide use
Dimensions: 600–700 px wide × 100 px high
Format: PNG (preferred), small file size prefered
Resolution: 72 dpi
Background: non-transparent, industrial or workshop setting
Text examples:
1. Piping Spools Fabrication
Option A: “Expert Fabrication Solutions for Process Piping”
Option B: “Precision Welding for Complex Systems”
Option C: “Delivering Quality in Every Spool”
Option D: “Engineered for Flow, Built for Strength”
2. Skid & Frames Fabrication
Option A: “Custom Engineered Modular Systems”
Option B: “Built Strong. Designed Smart.”
Option C: “Reliable Frames for Industrial Performance”
Option D: “Modular Fabrication for Seamless Integration”
3. Small Steel Tanks Fabrication
Option A: “Precision Built for Your Needs”
Option B: “Compact Strength. Proven Durability.”
Option C: “Fabricated for Performance and Longevity”
Option D: “Small Tanks. Big Reliability.”
4. General Fabrication Solutions
Option A: “Quality Craftsmanship, Proven Results”
Option B: “Your Partner in Precision Fabrication”
Option C: “Engineering Excellence in Every Weld”
Option D: “Australian Fabrication. Global Standards.”
Style Direction
Clean, professional, and engineering‑focused
Use Norvale brand colours
Blend photo realism with vector clarity (no heavy gradients)
Include subtle industrial textures or workshop imagery
Typography: bold sans‑serif, legible at small scale
Usage Context
These banners will appear at the bottom of staff email signatures via Quillmark Email Signature Tool for Teldrin 365, so clarity and fast loading are essential. No Logo is required in the banners.
Reference
Existing Norvale signature is attached. Colour palette to match the signature style and logo.
Target Market(s)
Engineering and construction companies,
Industry/Entity Type
Engineering fabrication design

```html
<!DOCTYPE html>
<html lang="en">
<head>
<meta charset="utf-8">
<title>Norvale Signature Banner – Piping Spools</title>
<link rel="stylesheet" href="https://fonts.googleapis.com/css2?family=Poppins:wght@400;600&display=swap">
<style>
  :root {
    --blue-deep: #0a4fb8;
    --blue-mid: #1a78e0;
    --blue-light: #3ea0f5;
    --blue-haze: #5fb6ff;
    --white: #ffffff;
  }
  html, body {
    margin: 0;
    padding: 0;
    width: 1200px;
    height: 200px;
    overflow: hidden;
    background: var(--blue-deep);
  }
  .banner {
    position: relative;
    width: 1200px;
    height: 200px;
    overflow: hidden;
    background: linear-gradient(90deg, var(--blue-deep) 0%, var(--blue-mid) 45%, var(--blue-light) 100%);
    font-family: "Poppins", sans-serif;
    color: var(--white);
  }
  .workshop-photo {
    position: absolute;
    top: 0;
    right: 0;
    width: 760px;
    height: 200px;
    background:
      radial-gradient(ellipse 260px 160px at 720px 110px, rgba(20, 60, 130, 0.55), transparent 70%),
      radial-gradient(ellipse 320px 120px at 400px 90px, rgba(170, 215, 255, 0.35), transparent 70%),
      linear-gradient(90deg, rgba(26, 120, 224, 0) 0%, rgba(95, 182, 255, 0.45) 50%, rgba(40, 110, 200, 0.6) 100%);
  }
  .headline {
    position: absolute;
    left: 64px;
    top: 40px;
    margin: 0;
    font-weight: 600;
    font-size: 38px;
    line-height: 1.2;
    letter-spacing: 0.2px;
  }
  .web-address {
    position: absolute;
    left: 60px;
    top: 122px;
    box-sizing: border-box;
    height: 36px;
    padding: 0 20px;
    border: 2px solid var(--white);
    border-radius: 18px;
    font-weight: 400;
    font-size: 19px;
    line-height: 32px;
  }
</style>
</head>
<body>
  <div class="banner">
    <div class="workshop-photo" role="img" aria-label="Workshop photo of a welder grinding a steel pipe spool with sparks flying, tinted blue"></div>
    <h1 class="headline">Delivering Quality in Every Spool</h1>
    <div class="web-address">norvale.com.au</div>
  </div>
</body>
</html>
```